Tolliver Partners
Business Cards, Letterhead, Envelope and 3-4 basic Power Point Slides
Tolliver Partners -
Creative Brief
Please submit designs for: Business Cards, Letterhead, No. 10 Envelope and 3-4 Basic Power Point Slides Please see our web site for more information: TolliverPartners.com
Corporate and Investor Services
We have already completed our logo and its is available for downloading. Please do not make changes to the logo.

```html
<!DOCTYPE html>
<html lang="en">
<head>
<meta charset="utf-8">
<title>Tolliver Partners – Stationery and Slide Templates</title>
<link rel="stylesheet" href="https://fonts.googleapis.com/css2?family=Open+Sans:wght@400;700&display=swap">
<style>
  :root{
    --blue:#1d5ca8;
    --blue-light:#4c8fd4;
    --green:#3d9b35;
    --green-light:#8cc63f;
    --paper:#ffffff;
    --bg:#ffffff;
    --ink:#1d5ca8;
    --label:#555555;
    --faint:#eef2ee;
  }
  *{box-sizing:border-box;margin:0;padding:0}
  html,body{width:1200px;height:350px;overflow:hidden;background:var(--bg);font-family:"Open Sans",Arial,sans-serif}
  .canvas{position:relative;width:1200px;height:350px}
  .label{position:absolute;font-size:5px;color:var(--label)}
  .piece{position:absolute;background:var(--paper);box-shadow:0 0 2px rgba(0,0,0,.35);overflow:hidden}
  .piece svg.shapes{position:absolute;inset:0;width:100%;height:100%}
  .brand{position:absolute;display:flex;align-items:center;gap:3px;color:var(--ink);font-weight:700;white-space:nowrap}
  .brand .dot{border-radius:50%;background:var(--green);flex:none}
  .small-text{position:absolute;color:var(--ink);font-size:3.5px;line-height:1.4}

  .letterhead{left:12px;top:18px;width:168px;height:322px}
  .envelope{left:190px;top:24px;width:182px;height:112px}
  .card-front{left:190px;top:236px;width:76px;height:56px}
  .card-back{left:284px;top:236px;width:88px;height:56px}
  .slide-front{left:598px;top:82px;width:272px;height:212px}
  .slide-inside{left:886px;top:82px;width:300px;height:220px}

  .slide-title{position:absolute;color:var(--blue);font-weight:400}
  .photo{position:absolute;background:linear-gradient(120deg,#c9d7ea 0%,#6e8fb8 45%,#1f3558 100%)}
  .picture-box{position:absolute;border:1px solid var(--blue);display:flex;align-items:center;justify-content:center;color:var(--blue);font-size:15px;background:#fff}
  .body-copy{position:absolute;color:var(--blue);font-size:9.5px;line-height:1.25}
</style>
</head>
<body>
<div class="canvas">

  <!-- Letterhead -->
  <span class="label" style="left:12px;top:10px">Letter Head</span>
  <section class="piece letterhead">
    <svg class="shapes" viewBox="0 0 168 322" preserveAspectRatio="none" aria-hidden="true">
      <circle cx="40" cy="250" r="42" fill="var(--faint)"/>
      <path d="M0 300 C50 318 110 300 168 262 L168 322 L0 322 Z" fill="var(--green)"/>
      <path d="M0 310 C60 325 120 305 168 280 L168 322 L0 322 Z" fill="var(--blue)"/>
    </svg>
    <div class="brand" style="left:58px;top:16px;font-size:6px">
      <span class="dot" style="width:9px;height:9px"></span>Tolliver Partners
    </div>
    <div class="small-text" style="left:8px;top:286px">12 Harbor Street, Springfield<br>Tel 555-0142 · TolliverPartners.com</div>
  </section>

  <!-- Envelope -->
  <span class="label" style="left:214px;top:16px">Envelope</span>
  <section class="piece envelope">
    <svg class="shapes" viewBox="0 0 182 112" preserveAspectRatio="none" aria-hidden="true">
      <circle cx="155" cy="30" r="30" fill="var(--faint)"/>
      <path d="M100 112 C140 100 165 70 182 40 L182 112 Z" fill="var(--green)"/>
      <path d="M125 112 C155 104 172 85 182 62 L182 112 Z" fill="var(--blue)"/>
    </svg>
    <div class="brand" style="left:8px;top:8px;font-size:5px">
      <span class="dot" style="width:8px;height:8px"></span>Tolliver Partners
    </div>
    <div class="small-text" style="left:8px;top:20px">12 Harbor Street</div>
  </section>

  <!-- Business card front -->
  <span class="label" style="left:190px;top:228px">Bus Card</span>
  <section class="piece card-front">
    <svg class="shapes" viewBox="0 0 76 56" preserveAspectRatio="none" aria-hidden="true">
      <path d="M0 50 C25 56 55 48 76 36 L76 56 L0 56 Z" fill="var(--green)"/>
      <path d="M20 56 C45 54 62 48 76 44 L76 56 Z" fill="var(--blue)"/>
    </svg>
    <div class="brand" style="left:5px;top:5px;font-size:4px">
      <span class="dot" style="width:6px;height:6px"></span>Tolliver Partners
    </div>
    <div class="small-text" style="left:5px;top:22px;font-size:3px">Jordan Avery<br>Managing Partner<br>555-0142</div>
  </section>

  <!-- Business card back -->
  <span class="label" style="left:284px;top:228px">Back</span>
  <section class="piece card-back" style="background:var(--blue)">
    <svg class="shapes" viewBox="0 0 88 56" preserveAspectRatio="none" aria-hidden="true">
      <rect width="88" height="56" fill="var(--blue-light)"/>
      <path d="M0 0 L88 0 L88 20 C60 34 30 30 0 40 Z" fill="var(--blue)"/>
      <path d="M0 46 C30 40 60 44 88 30 L88 56 L0 56 Z" fill="var(--green)"/>
    </svg>
  </section>

  <!-- Slide: front -->
  <span class="label" style="left:620px;top:74px">PowerPoint Template Front</span>
  <section class="piece slide-front">
    <svg class="shapes" viewBox="0 0 272 212" preserveAspectRatio="none" aria-hidden="true">
      <path d="M120 0 L272 0 L272 212 L90 212 C150 160 110 60 120 0 Z" fill="var(--green)"/>
      <path d="M150 0 L272 0 L272 212 L120 212 C180 160 140 60 150 0 Z" fill="var(--blue)"/>
      <path d="M0 212 L0 150 C30 190 80 200 130 212 Z" fill="var(--green)"/>
    </svg>
    <h1 class="slide-title" style="left:14px;top:12px;font-size:18px">TITLE</h1>
    <div class="brand" style="left:96px;top:86px;font-size:11px;background:#fff;padding:3px 5px;border-radius:2px">
      <span class="dot" style="width:14px;height:14px"></span>Tolliver Partners
    </div>
    <div class="photo" role="img" aria-label="Business team silhouettes in front of a globe with an airplane overhead" style="left:150px;top:122px;width:118px;height:86px"></div>
  </section>

  <!-- Slide: inside -->
  <span class="label" style="left:886px;top:74px">PowerPoint Template Inside</span>
  <section class="piece slide-inside">
    <svg class="shapes" viewBox="0 0 300 220" preserveAspectRatio="none" aria-hidden="true">
      <path d="M0 220 L0 195 C80 215 200 200 300 150 L300 220 Z" fill="var(--green)"/>
      <path d="M0 220 C100 220 220 205 300 170 L300 220 Z" fill="var(--blue)"/>
      <path d="M0 18 L300 18" stroke="var(--blue)" stroke-width="1"/>
    </svg>
    <div class="brand" style="left:8px;top:4px;font-size:5px">
      <span class="dot" style="width:8px;height:8px"></span>Tolliver Partners
    </div>
    <h1 class="slide-title" style="left:12px;top:40px;font-size:26px">TITLE</h1>
    <p class="body-copy" style="left:132px;top:28px;width:160px">Lorem ipsum dolor sit amet, consectetur adipiscing elit. Nullam ullamcorper, odio sit amet aliquet porta, lectus leo ornare nisi, eu egestas felis dolor quis ante.</p>
    <div class="picture-box" style="left:172px;top:100px;width:118px;height:68px">Picture</div>
  </section>

</div>
</body>
</html>
```